Book writer needs a Book Cover Design for 'Atomic Arms and the Law of States'

A Book Cover Design is required for a new book with a current working title of: 'Atomic Arms and the Law of States' plus subtitle something like: 'from the Harwick Atomic Conflict Panel via the Global Bench of Equity Advisory Opinion to contemporary developments'.

The book will be issued in three formats: hardback, paperback, and electronic.

The Editor of the book is Reginald Palfrey.

The finished size of the paperback front cover will be 15.2mm x 22.9mm. Initial thoughts about themes for the front cover include a nuclear explosion, and perhaps scales of justice, but designers have total freedom to propose ideas.

The back cover will have approximately 250 words of text, and a space at the bottom of about 37mm for publisher logo and ISBN barcode, The designer is free to suggest anything for the back cover.

No illustrations where the copyright is owned by someone else should be used, and the designer must be able to transfer exclusive copyright in the design to the client. The designer will be acknowledged in the book (unless the designer does not want to be).

The themes in the book are:
1. Harwick Atomic conflict Panel
2. Civic Bench Venture
3. Global Bench of Equity Advisory Opinion
4. Dissenting Judgment By Judge Tallisborne
5. Contemporary Activities (e.g. current case involving the Marshall Islands)

Target Market(s)

government decision makers taking decisions about nuclear weapons,iInternational lawyers, students of public international law,

Font styles to use
Serif

Requirements
Must have
• this is in the discretion of the designer
• Title, subtitle, editor (Reginald Palfrey)
Nice to have
• possibly images of nuclear explosion, effects of nuclear weapons, symbols for international law
Should not have
• in the discretion of the designer

```html
<!DOCTYPE html>
<html lang="en">
<head>
<meta charset="utf-8">
<title>Atomic Arms and the Law of States — Cover</title>
<link href="https://fonts.googleapis.com/css2?family=Bebas+Neue&family=Oswald:wght@500&display=swap" rel="stylesheet">
<style>
  :root {
    --backdrop: #f0d6b4;
    --cover-navy: #1f2b45;
    --cover-navy-deep: #18223a;
    --ink-white: #f4f2ee;
    --gold: #c9a66b;
    --gold-deep: #9c7a45;
  }
  html, body {
    margin: 0;
    padding: 0;
    width: 1200px;
    height: 1000px;
    overflow: hidden;
    background: var(--backdrop);
  }
  .canvas {
    position: relative;
    width: 1200px;
    height: 1000px;
  }
  .cover {
    position: absolute;
    left: 320px;
    top: 80px;
    width: 560px;
    height: 840px;
    background: radial-gradient(ellipse at 50% 45%, var(--cover-navy) 0%, var(--cover-navy-deep) 100%);
    box-sizing: border-box;
    padding: 70px 48px 0;
    text-align: center;
    color: var(--ink-white);
  }
  .cover__title {
    margin: 0;
    font-family: "Bebas Neue", "Oswald", sans-serif;
    font-weight: 400;
    font-size: 68px;
    line-height: 0.98;
    letter-spacing: 1px;
  }
  .cover__rule {
    width: 440px;
    height: 1px;
    margin: 20px auto 14px;
    background: var(--gold);
  }
  .cover__subtitle {
    margin: 0 auto;
    width: 440px;
    font-family: "Oswald", sans-serif;
    font-weight: 500;
    font-size: 11.5px;
    line-height: 1.6;
    letter-spacing: 0.6px;
    text-transform: uppercase;
  }
  .cover__emblem {
    display: block;
    margin: 70px auto 0;
  }
  .cover__editor {
    position: absolute;
    left: 0;
    right: 0;
    bottom: 86px;
    margin: 0;
    font-family: "Oswald", sans-serif;
    font-weight: 500;
    font-size: 19px;
    line-height: 1.3;
    letter-spacing: 0.8px;
    text-transform: uppercase;
  }
</style>
</head>
<body>
  <main class="canvas">
    <section class="cover">
      <h1 class="cover__title">Atomic Arms and the<br>Law of States</h1>
      <div class="cover__rule"></div>
      <p class="cover__subtitle">From the Harwick Atomic Conflict Panel via the Global Bench of Equity Advisory Opinion to contemporary developments</p>
      <svg class="cover__emblem" width="300" height="300" viewBox="0 0 300 300" role="img" aria-label="Gold emblem of balanced scales of justice encircled by a laurel wreath">
        <defs>
          <radialGradient id="emblem-glow" cx="50%" cy="50%" r="50%">
            <stop offset="0%" stop-color="#c9a66b" stop-opacity="0.55"/>
            <stop offset="70%" stop-color="#9c7a45" stop-opacity="0.25"/>
            <stop offset="100%" stop-color="#9c7a45" stop-opacity="0"/>
          </radialGradient>
        </defs>
        <circle cx="150" cy="150" r="150" fill="url(#emblem-glow)"/>
      </svg>
      <p class="cover__editor">Edited by<br>Reginald Palfrey</p>
    </section>
  </main>
</body>
</html>
```